PROPERTY BROCHURE

Need an attractive layout and design for this multi-page brochure

Industry/Entity Type

Real Estate Development

Colors

Designer to choose colors to be used in the design.

```html
<!DOCTYPE html>
<html lang="en">
<head>
<meta charset="utf-8">
<title>Property Brochure – Sample Project Spread</title>
<link rel="stylesheet" href="https://fonts.googleapis.com/css2?family=Open+Sans:wght@400;600;700&display=swap">
<style>
  :root {
    --backdrop: #d4d4d4;
    --page-dark: #272728;
    --page-dark-edge: #1c1c1d;
    --accent-teal: #3f7f8d;
    --frame-teal: #3b6f7a;
    --tray-light: #e4e4e4;
    --card-border: #2a2a2a;
    --text-light: #e8e8e8;
  }
  * { box-sizing: border-box; margin: 0; padding: 0; }
  html, body {
    width: 1200px; height: 566px; overflow: hidden;
    background: var(--backdrop);
    font-family: "Open Sans", Arial, sans-serif;
  }
  .spread {
    position: absolute; left: 20px; top: 74px;
    width: 1160px; height: 418px;
    display: flex;
  }
  .page {
    position: relative; width: 580px; height: 418px;
    overflow: hidden;
  }
  .page--left { background: linear-gradient(90deg, var(--page-dark) 82%, var(--page-dark-edge)); }
  .page--right { background: linear-gradient(90deg, var(--page-dark-edge), var(--page-dark) 14%); }
  .section-title {
    position: absolute; color: var(--accent-teal);
    font-weight: 700; font-size: 17px; line-height: 20px; letter-spacing: 0.2px;
  }
  .project-summary, .step-list {
    position: absolute; color: var(--text-light); font-size: 13.5px; line-height: 23px;
    list-style: none; white-space: nowrap;
  }
  .step-list li, .project-summary .figure { padding-left: 20px; position: relative; }
  .step-list li::before, .project-summary .figure::before {
    content: ""; position: absolute; left: 1px; top: 9px;
    width: 5px; height: 5px; border: 1px solid var(--text-light); border-radius: 50%;
  }
  .page--left .section-title { left: 154px; top: 36px; }
  .page--left .project-summary { left: 154px; top: 60px; }
  .page--right .section-title { left: 34px; top: 32px; }
  .page--right .step-list { left: 34px; top: 56px; }

  .render-tray {
    position: absolute; left: 17px; top: 213px; width: 554px; height: 210px;
    background: var(--tray-light); border: 5px solid var(--frame-teal);
    border-bottom: none; border-radius: 10px 10px 0 0;
  }
  .render-card {
    position: absolute; top: 15px; width: 165px; height: 200px;
    border: 3px solid var(--card-border); border-bottom: none; border-radius: 8px 8px 0 0;
  }
  .render-card--kitchen { left: 13px; background: linear-gradient(180deg, #e2e0dd 0%, #cfcbc6 45%, #a8a39c 75%, #6e6a66 100%); }
  .render-card--facade { left: 193px; background: linear-gradient(180deg, #7f98b4 0%, #a9b6c1 22%, #8a7f72 40%, #9b5a42 58%, #5f8f3e 76%, #3f7a2d 94%, #b8b8b4 100%); }
  .render-card--dining { left: 373px; background: linear-gradient(180deg, #dcd9d4 0%, #c9c5be 50%, #8f8a84 80%, #5e5a56 100%); }

  .photo-frame {
    position: absolute; border: 5px solid var(--frame-teal); border-radius: 10px;
  }
  .photo-frame--tram {
    left: 269px; top: 14px; width: 320px; height: 178px; border-right: none;
    border-radius: 10px 0 0 10px;
    background: linear-gradient(180deg, #3e7a3e 0%, #c99a3e 22%, #d9ae4c 45%, #2f6a4a 55%, #e0c45a 62%, #d9b64e 85%, #3a3a3a 100%);
  }
  .photo-frame--skyline {
    left: 17px; top: 211px; width: 549px; height: 214px; border-bottom: none;
    border-radius: 10px 10px 0 0;
    background: linear-gradient(180deg, #2f6cb0 0%, #5a8fc4 30%, #9fb7cc 48%, #c7a27a 56%, #2e3744 64%, #3a3f48 72%, #8a7a5a 80%, #4a5260 100%);
  }
</style>
</head>
<body>
  <main class="spread">
    <section class="page page--left">
      <h2 class="section-title">SAMPLE PROJECT</h2>
      <ul class="project-summary">
        <li>3 Townhouse development in Maple Heights</li>
        <li class="figure">Purchase Price:&nbsp; $715,000</li>
        <li class="figure">Re-development costs: $892,500</li>
        <li class="figure">Target sale price: $2,150,000</li>
        <li class="figure">Net profit: $269,200</li>
      </ul>
      <div class="render-tray">
        <div class="render-card render-card--kitchen" role="img" aria-label="Interior render of a modern kitchen and dining area"></div>
        <div class="render-card render-card--facade" role="img" aria-label="Exterior render of a two-storey brick townhouse with front lawn"></div>
        <div class="render-card render-card--dining" role="img" aria-label="Interior render of a dining room with bar stools"></div>
      </div>
    </section>
    <section class="page page--right">
      <h2 class="section-title">NEXT STEPS</h2>
      <ul class="step-list">
        <li>Non-Disclosure Agreement</li>
        <li>Proof of funds</li>
        <li>Terms and legal structure</li>
        <li>Memorandum of understanding</li>
        <li>Options for funding</li>
      </ul>
      <div class="photo-frame photo-frame--tram" role="img" aria-label="Photo of a vintage yellow and green city tram"></div>
      <div class="photo-frame photo-frame--skyline" role="img" aria-label="Photo of a waterfront city skyline at dusk with an observation wheel"></div>
    </section>
  </main>
</body>
</html>
```